KVO-Business Card Design

I need a modern, professional business card design that includes my logo as the main feature, maybe the entire background with the contact info overlaying or even contact info on the back and the logo full frontal

Neat and organized placement of contact information

Would like to see options in black and white

Target Market(s)

real estate Developers, Construction managers, business and home owners

Industry/Entity Type

Construction

Contact Information for Business Card

KVO Construction
Danny Ferrante
General Contractor

Office: 1-888-902-7315 Ext #1
Cell: 215-730-4162
Fax: 1-888-902-7315

Font styles to use
Serif

Requirements
Must have
• title
• office #
• cell #
• Email
• website
Nice to have
• fax

```html
<!DOCTYPE html>
<html lang="en">
<head>
<meta charset="utf-8">
<title>KVO Construction – Business Card</title>
<link rel="stylesheet" href="https://fonts.googleapis.com/css2?family=Open+Sans:wght@400;600;700&display=swap">
<style>
  :root {
    --page: #ecebe7;
    --card-dark: #323233;
    --card-dark-glow: #3c3c3d;
    --green: #9cc35a;
    --green-mid: #7ea955;
    --green-text: #a8cc4a;
    --white: #ffffff;
  }
  * { margin: 0; padding: 0; box-sizing: border-box; }
  html, body {
    width: 1200px; height: 843px; overflow: hidden;
    background: var(--page);
    font-family: "Open Sans", sans-serif;
  }
  .sheet { position: relative; width: 1200px; height: 843px; }
  .card {
    position: absolute; width: 560px; height: 320px;
    background: var(--card-dark); overflow: hidden;
    box-shadow: 0 8px 22px rgba(0,0,0,.18);
  }
  .card--front {
    left: 120px; top: 80px;
    background: radial-gradient(ellipse at 50% 45%, var(--card-dark-glow) 0%, var(--card-dark) 65%);
  }
  .card--back { left: 520px; top: 443px; }

  .brand { position: absolute; display: flex; align-items: center; gap: 12px; }
  .brand__mark { background: var(--green); }
  .brand__name { color: var(--green-text); font-weight: 700; white-space: nowrap; }

  .card--front .brand { left: 50%; top: 50%; transform: translate(-50%, -50%); }
  .card--front .brand__mark { width: 26px; height: 26px; }
  .card--front .brand__name { font-size: 40px; letter-spacing: .5px; }

  .card--back .brand { right: 26px; top: 40px; gap: 8px; }
  .card--back .brand__mark { width: 14px; height: 14px; }
  .card--back .brand__name { font-size: 20px; }

  .band {
    position: absolute; left: 0; right: 0; top: 190px; bottom: 0;
    background: linear-gradient(90deg, var(--green-mid) 0%, var(--green) 100%);
  }

  .person { position: absolute; left: 40px; top: 110px; }
  .person__name { color: var(--green-text); font-size: 24px; font-weight: 700; }
  .person__title { color: var(--white); font-size: 14px; margin-top: 2px; }

  .contact { position: absolute; left: 352px; top: 206px; list-style: none; }
  .contact li {
    display: flex; align-items: center; gap: 10px;
    color: var(--white); font-size: 13px; line-height: 20px;
  }
  .contact svg { width: 12px; height: 12px; flex: none; }
</style>
</head>
<body>
<main class="sheet">

  <section class="card card--front" aria-label="Card front">
    <div class="brand">
      <span class="brand__mark"></span>
      <span class="brand__name">KVO Construction</span>
    </div>
  </section>

  <section class="card card--back" aria-label="Card back">
    <div class="band" role="img" aria-label="Decorative green folded band graphic"></div>

    <div class="brand">
      <span class="brand__mark"></span>
      <span class="brand__name">KVO Construction</span>
    </div>

    <div class="person">
      <p class="person__name">Danny Ferrante</p>
      <p class="person__title">General Contractor</p>
    </div>

    <ul class="contact">
      <li><svg viewBox="0 0 12 12"><rect x="3" y="0.5" width="6" height="11" rx="1" fill="none" stroke="#fff"/><rect x="5" y="9.3" width="2" height="1" fill="#fff"/></svg>215-730-4162</li>
      <li><svg viewBox="0 0 12 12"><path d="M1 4 Q6 0 11 4 L9 5.5 L8 4 L4 4 L3 5.5 Z" fill="#fff"/><rect x="2" y="6" width="8" height="5" rx="1" fill="#fff"/></svg>1-888-902-7315 Ext #1</li>
      <li><svg viewBox="0 0 12 12"><rect x="3" y="0.5" width="6" height="4" fill="none" stroke="#fff"/><rect x="0.5" y="4.5" width="11" height="5" fill="#fff"/><rect x="3" y="8" width="6" height="3.5" fill="#fff" stroke="#9cc35a" stroke-width=".6"/></svg>1-888-902-7315</li>
      <li><svg viewBox="0 0 12 12"><circle cx="6" cy="6" r="5.3" fill="none" stroke="#fff"/><ellipse cx="6" cy="6" rx="2.3" ry="5.3" fill="none" stroke="#fff"/><line x1="0.7" y1="6" x2="11.3" y2="6" stroke="#fff"/></svg>www.kvobuild.com</li>
      <li><svg viewBox="0 0 12 12"><rect x="0.5" y="2.5" width="11" height="7.5" fill="#fff"/><polyline points="0.5,2.5 6,7 11.5,2.5" fill="none" stroke="#9cc35a"/></svg>office@kvobuild.com</li>
    </ul>
  </section>

</main>
</body>
</html>
```